Website design for an HR and wellness consultant

Lantern Grove Website Development Brief

The scope of this project is to design a website for Lantern Grove. In particular, this will require the designer to:

1. Design and build a website based on the site- map provided. The existing brand (the logo and colours) should be incorporated throughout the website design.

2. Change 2 of the colours from the existing logo

About Lantern Grove:
Lantern Grove’s core vision is to support both individuals and organisations with growing to reach their full potential.
At an organisational level, we do this through training, consulting, leadership development, facilitation, coaching and corporate wellness programs.

About the Brand:
Lantern Grove offers services that cover the spectrum from corporate human resources through to wellness and personal development. The personal development aspect of the business incorporating some aspects of both a wellbeing and spiritual nature.

Like the logo, the website must communicate an earthy, natural yet professional image.

Website Structure and Content:
Lantern Grove would like to create a clean and simple website that is visually appealing, easy to navigate and not overladen with functionality.

Please refer to the file "Website copy" for connecting each of the supplied images to the pages of the site.

Please note the quotations in the website copy should be paired with the images on each page.
Updates

Project Deadline Extended
Reason: Hi There, I am extending the deadline by one day as this project has not been delivered and there are still too many files that required amendments and approval at this stage. Thanks, Megan

Target Market(s)

Human resources decision makers in medium to large organisations - and individuals interested in personal development.

Industry/Entity Type

Leadership

Requirements
Must have
• It is important that the look and feel of the website is able to appeal to both a corporate audience as well as to individuals who are drawn to the wellbeing/wellness services too.

It should look professional enough for the corporate audience, but not too austere and clinical for those that are drawn to the more esoteric side of the business.

The logo should appear on each page of the website.

All text must be aligned/justified to the left and to the right.
Must include a web form on the ‘Contact Us’ page to capture fields of contact data.
Should not have
• Please don't use bold colours like strong reds or yellows.

```html
<!DOCTYPE html>
<html lang="en">
<head>
<meta charset="utf-8">
<title>Lantern Grove</title>
<link rel="stylesheet" href="https://fonts.googleapis.com/css2?family=Cuprum:ital,wght@0,400;0,700;1,400&family=PT+Sans:ital,wght@0,400;1,400&display=swap">
<style>
:root{
  --brown-deep:#6a3604;
  --brown:#7b420b;
  --brown-text:#6b3306;
  --cream:#efe4c8;
  --cream-light:#f7efdc;
  --gold-top:#fde49a;
  --gold-bottom:#f2b13a;
  --gold-text:#6b3a08;
  --body-text:#4a4a4a;
  --line:#d8d8d8;
  --white:#ffffff;
  --footer-text:#f0d8b0;
}
*{box-sizing:border-box;margin:0;padding:0}
html,body{width:1150px;height:1200px;overflow:hidden}
body{
  position:relative;
  background:linear-gradient(180deg,var(--brown-deep) 0%,var(--brown) 100%);
  font-family:"PT Sans",Arial,sans-serif;
  color:var(--body-text);
}
.contact-bar{position:absolute;left:0;top:0;width:1150px;height:46px}
.contact-bar svg{position:absolute;left:0;top:0}
.contact-line{
  position:absolute;left:442px;top:12px;
  font-family:"Cuprum",Arial,sans-serif;font-size:17px;color:var(--brown-text);
  letter-spacing:.4px;white-space:nowrap;
}
.contact-line .sep{margin:0 18px}
.search{
  position:absolute;left:872px;top:11px;width:182px;height:21px;
  border-radius:11px;background:var(--white);border:1px solid #d9cfb8;
  font-size:11px;font-style:italic;color:#aaa;padding:3px 0 0 17px;
}
.search svg{position:absolute;right:8px;top:4px}
.brand{position:absolute;left:104px;top:74px;display:flex;align-items:center;gap:10px}
.brand-dot{width:16px;height:16px;border-radius:50%;background:#c9a02a}
.brand-name{font-family:"PT Sans",Arial,sans-serif;font-size:28px;color:var(--cream);letter-spacing:1px}
.main-nav{position:absolute;left:449px;top:100px;display:flex;gap:2px}
.main-nav a{
  display:block;width:118px;height:48px;border-radius:12px 12px 0 0;
  background:linear-gradient(180deg,var(--gold-top),var(--gold-bottom));
  font-style:italic;font-size:15px;color:var(--gold-text);
  text-align:center;padding-top:16px;text-decoration:none;
  border:1px solid #e0a040;border-bottom:none;
}
.main-nav a.is-active{background:linear-gradient(180deg,#fafafa 0%,#eceded 60%,#c9cbcd 100%);border-color:#ddd;color:#3b2a14}
.page{
  position:absolute;left:94px;top:148px;width:964px;height:962px;
  background:var(--white);border-radius:4px 4px 8px 8px;
  box-shadow:0 2px 6px rgba(0,0,0,.3);
}
.hero-zone{position:absolute;left:0;top:0;width:964px;height:400px;background:linear-gradient(180deg,#fff,#f5f5f5);border-bottom:1px solid var(--line)}
.slider-frame{position:absolute;left:14px;top:10px;width:937px;height:313px;border-radius:16px;background:var(--white);border:1px solid #e2e2e2;box-shadow:0 1px 4px rgba(0,0,0,.12)}
.slide{
  position:absolute;left:9px;top:10px;width:917px;height:292px;border-radius:12px;
  background:radial-gradient(ellipse at 40% 50%,#f1ead2 0%,#e8dfc0 60%,#dcd1ad 100%);
  border:1px solid #cdbd8c;
}
.slide-quote{position:absolute;right:74px;top:92px;text-align:right;font-family:"Cuprum",Arial,sans-serif;font-size:27px;line-height:31px;color:#3e3e3e;letter-spacing:.4px}
.slide-quote cite{display:block;margin-top:7px;font-size:20px;font-style:italic;color:#4a3a20;letter-spacing:1px}
.slide-dots{position:absolute;right:18px;bottom:13px;display:flex;gap:5px}
.slide-dots span{width:13px;height:13px;border-radius:50%;background:var(--brown-deep)}
.hero-caption{position:absolute;left:41px;top:339px;width:885px;font-size:12px;line-height:20px;color:#555}
.intro{position:absolute;left:16px;top:411px;width:933px}
.intro h1,.services h2{font-family:"Cuprum",Arial,sans-serif;font-weight:700;color:var(--brown-text)}
.intro h1{font-size:23px;margin-bottom:9px}
.intro p{font-size:11.3px;line-height:18px;margin-bottom:6px;text-align:justify;color:#4d4d4d}
.intro p.tight{margin-bottom:2px}
.divider{position:absolute;left:16px;top:700px;width:932px;border-top:2px dotted #b8b8b8}
.services h2{position:absolute;left:30px;top:721px;font-size:19px}
.card{position:absolute;top:755px;width:466px;height:189px;border:1px solid #d6d6d6;border-radius:8px;background:var(--white)}
.card--left{left:15px}
.card--right{left:486px}
.card-photo{position:absolute;left:12px;top:19px;width:160px;height:120px;border-radius:5px;border:1px solid #bbb}
.card--left .card-photo{background:linear-gradient(180deg,#6c86a6 0%,#9cb0c8 60%,#c9b48c 72%,#a88c62 100%)}
.card--right .card-photo{background:linear-gradient(180deg,#2e6fc2 0%,#7fb2e6 55%,#6a9a4a 75%,#4c8a2a 100%)}
.card h3{position:absolute;left:180px;top:14px;font-family:"Cuprum",Arial,sans-serif;font-weight:400;font-size:16px;color:var(--brown-text)}
.card p{position:absolute;left:180px;top:40px;width:272px;font-size:11.5px;line-height:20px;text-align:justify;color:#555}
.btn{
  position:absolute;right:10px;top:147px;width:81px;height:25px;border-radius:4px;
  background:linear-gradient(180deg,#9a5a24,#6a3404);color:#fbe8c8;
  font-style:italic;font-size:12.5px;text-align:center;padding-top:4px;text-decoration:none;
  box-shadow:0 1px 2px rgba(0,0,0,.35);
}
.footer-nav{position:absolute;left:0;top:1134px;width:1150px;text-align:center;font-size:12px;color:var(--footer-text)}
.footer-nav a{color:var(--footer-text);text-decoration:none}
.footer-nav .sep{margin:0 14px}
.copyright{position:absolute;left:0;top:1164px;width:1150px;text-align:center;font-size:12px;color:var(--footer-text)}
</style>
</head>
<body>
<header>
  <div class="contact-bar">
    <svg width="1150" height="46" viewBox="0 0 1150 46" aria-hidden="true">
      <defs><linearGradient id="barFill" x1="0" y1="0" x2="0" y2="1"><stop offset="0" stop-color="#f6edd6"/><stop offset="1" stop-color="#e4d4ae"/></linearGradient></defs>
      <path d="M0 0 H1150 V44 H430 C405 44 405 0 360 0 Z" fill="none"/>
      <path d="M370 0 C400 2 408 44 432 44 H1150 V0 Z" fill="url(#barFill)"/>
    </svg>
    <div class="contact-line">Phone :&nbsp; : &nbsp;+61 03 9000 4521<span class="sep">|</span>Mobile : &nbsp;0400 555 219</div>
    <div class="search">Search
      <svg width="12" height="12" viewBox="0 0 12 12" aria-hidden="true"><circle cx="4.5" cy="4.5" r="3.4" fill="none" stroke="#888" stroke-width="1.3"/><line x1="7" y1="7" x2="11" y2="11" stroke="#888" stroke-width="1.6"/></svg>
    </div>
  </div>
  <div class="brand"><span class="brand-dot"></span><span class="brand-name">Lantern Grove</span></div>
  <nav class="main-nav">
    <a class="is-active" href="#">Home</a>
    <a href="#">About us</a>
    <a href="#">Services</a>
    <a href="#">Profile</a>
    <a href="#">Contact us</a>
  </nav>
</header>

<main class="page">
  <section class="hero-zone">
    <div class="slider-frame">
      <div class="slide" role="img" aria-label="Young green seedling growing from pale sand">
        <blockquote class="slide-quote">The best way to predict the future<br>is to create it.<cite>Harlan J. Whitcombe</cite></blockquote>
        <div class="slide-dots"><span></span><span></span><span></span><span></span></div>
      </div>
    </div>
    <p class="hero-caption">Sed ut perspiciatis unde omnis iste natus error sit voluptatem accusantium doloremque laudantium, totam rem aperiam, eaque ipsa quae ab illo inventore veritatis et quasi architecto beatae vitae dicta sunt explicabo. Nemo enim ipsam voluptatem quia voluptas sit aspernatur aut odit aut fugit</p>
  </section>

  <section class="intro">
    <h1>Welcome to our site</h1>
    <p>Lantern Grove’s core vision is to support both individuals and organisations with growing to reach their full potential.</p>
    <p>At an organisational level, we do this through training, consulting, leadership development, facilitation, coaching and corporate wellness programs.</p>
    <p>Our key point of difference when working with businesses is an innovative yet structured approach that results in real and lasting change. Our experience and expertise has resulted in significant outcomes for the clients we have worked with, including:</p>
    <p>Sed ut perspiciatis unde omnis iste natus error sit voluptatem accusantium doloremque laudantium, totam rem aperiam, eaque ipsa quae ab illo inventore veritatis et quasi architecto beatae vitae dicta sunt explicabo. Nemo enim ipsam voluptatem quia voluptas sit aspernatur aut odit aut fugit, sed quia consequuntur magni dolores eos qui ratione voluptatem sequi nesciunt. Neque porro quisquam est, qui dolorem ipsum quia dolor sit amet, consectetur, adipisci velit, sed quia non numquam eius modi tempora incidunt ut labore et dolore magnam aliquam quaerat voluptatem. Ut enim ad minima veniam, quis nostrum exercitationem ullam corporis suscipit laboriosam, nisi ut aliquid ex ea commodi consequatur.</p>
    <p>Quis autem vel eum iure reprehenderit qui in ea voluptate velit esse quam nihil molestiae consequatur, vel illum qui dolorem eum fugiat quo voluptas nulla pariatur. At vero eos et accusamus et iusto odio dignissimos ducimus qui blanditiis praesentium voluptatum deleniti atque corrupti quos dolores et quas molestias excepturi sint occaecati cupiditate non provident, similique sunt in culpa qui officia deserunt mollitia animi, id est laborum et dolorum fuga. Et harum quidem rerum facilis est et expedita distinctio.</p>
  </section>

  <div class="divider"></div>

  <section class="services">
    <h2>What We Do</h2>
    <article class="card card--left">
      <div class="card-photo" role="img" aria-label="Two business people shaking hands in an open field"></div>
      <h3>Neque porro quisquam</h3>
      <p>There are many variations of passages of Lorem Ipsum available, but the majority have suffered alteration in some form, by injected humour, or randomised words which don't look even slightly believable. If you are going to use a passage of Lorem Ipsum.</p>
      <a class="btn" href="#">View more</a>
    </article>
    <article class="card card--right">
      <div class="card-photo" role="img" aria-label="Person leaping joyfully on a green hill under a sunny sky"></div>
      <h3>Neque porro quisquam</h3>
      <p>There are many variations of passages of Lorem Ipsum available, but the majority have suffered alteration in some form, by injected humour, or randomised words which don't look even slightly believable. If you are going to use a passage of Lorem Ipsum.</p>
      <a class="btn" href="#">View more</a>
    </article>
  </section>
</main>

<footer>
  <nav class="footer-nav">
    <a href="#">Home</a><span class="sep">|</span><a href="#">About us</a><span class="sep">|</span><a href="#">Our Services</a><span class="sep">|</span><a href="#">Blog</a><span class="sep">|</span><a href="#">Contact us</a><span class="sep">|</span><a href="#">Sitemap</a>
  </nav>
  <p class="copyright">Copyright © 2012 www.lanterngrove.com &nbsp;&nbsp;All rights reserved.</p>
</footer>
</body>
</html>
```